Business Cards for Branding (Advertising) Agency

We need stylish and cool business cards.
Additional info:
1) Logo - see the attachment. You can use either the three penguins or just one penguin face (square or round) - at your discretion.
2) Text and other stuff for business card:
front side:
-Logo and company name: company name - Coastal Herons - should be in English as is in logo. This is the only exception. The rest of the text will be in Russian.
-Who we are: Брендинговое агентство
-First and last name:
-Position: Управляющий партнёр
-Address:
-Phone:
-Email:
-Website:
Note: please don't use names of information fields, such as: who we are, first and last name, position, address, phone, email and website.

3) Our suggestions on design:
-The backside of the business card can be either blank or has something on it - at your discretion.
-The business card background should be either white or grey (you can use any tone of grey).

Additional Information:
1) БРЕНДИНГОВОЕ АГЕНТСТВО
2) ул. Вересковая - these two words should be together on the same line
3) тел.: +7 (495) 381-62-09
моб.: +7 (916) 740-28-51

Reason: We would like to receive more stylish designs.

```html
<!DOCTYPE html>
<html lang="ru">
<head>
<meta charset="utf-8">
<title>Coastal Herons — визитная карточка</title>
<link rel="stylesheet" href="https://fonts.googleapis.com/css2?family=PT+Serif:wght@400;700&display=swap">
<style>
  :root {
    --stage: #262626;
    --paper: #ffffff;
    --ink: #141414;
    --accent: #f2a81d;
    --night: #0d0d0d;
    --light-text: #f4f4f4;
    --serif: "PT Serif", Georgia, serif;
  }
  * { box-sizing: border-box; margin: 0; padding: 0; }
  html, body {
    width: 1200px;
    height: 871px;
    overflow: hidden;
    background: var(--stage);
  }
  .business-card {
    position: absolute;
    left: 100px;
    top: 158px;
    width: 1000px;
    height: 556px;
    background: var(--paper);
    font-family: var(--serif);
    color: var(--ink);
    box-shadow: 0 18px 40px rgba(0,0,0,.45);
    overflow: hidden;
  }
  .person {
    position: absolute;
    right: 60px;
    top: 52px;
    text-align: right;
  }
  .person__name {
    font-size: 40px;
    font-weight: 400;
    letter-spacing: 1px;
  }
  .person__role {
    margin-top: 4px;
    font-size: 21px;
    font-weight: 700;
  }
  .brand {
    position: absolute;
    left: 64px;
    top: 176px;
    display: flex;
    align-items: center;
    gap: 18px;
  }
  .brand__dot {
    width: 26px;
    height: 26px;
    border-radius: 50%;
    background: var(--ink);
  }
  .brand__name {
    font-size: 50px;
    font-weight: 700;
    letter-spacing: 1px;
    color: var(--ink);
  }
  .tagline-band {
    position: absolute;
    left: 0;
    top: 302px;
    width: 100%;
    height: 46px;
    background: var(--accent);
  }
  .tagline {
    position: absolute;
    left: 64px;
    top: 5px;
    font-size: 30px;
    letter-spacing: 3px;
    color: var(--ink);
  }
  .contacts {
    position: absolute;
    left: 0;
    top: 348px;
    width: 100%;
    height: 208px;
    background: var(--night);
    color: var(--light-text);
    padding: 26px 64px 0;
    list-style: none;
    font-size: 25px;
    line-height: 38px;
    letter-spacing: .5px;
  }
</style>
</head>
<body>
  <article class="business-card">
    <header class="person">
      <h1 class="person__name">Мария Вольская</h1>
      <p class="person__role">Управляющий партнёр</p>
    </header>

    <div class="brand">
      <span class="brand__dot"></span>
      <span class="brand__name">Coastal Herons</span>
    </div>

    <div class="tagline-band">
      <p class="tagline">Брендинговое агентство</p>
    </div>

    <ul class="contacts">
      <li class="contacts__phone">+7 (916) 740-28-51</li>
      <li class="contacts__email">maria@coastalherons.ru</li>
      <li class="contacts__web">www.coastalherons.ru</li>
      <li class="contacts__address">117312, г. Москва, ул. Вересковая, д.12, стр.2</li>
    </ul>
  </article>
</body>
</html>
```